Fun family flyer for photographer

Need a flyer to promote our business moving to Brisbane.

Require a family friendly look targetted to mothers, using our logo and existing images from previous shoots.

Would like to see designs that feature the images heavily, but still have text and fonts that set it aside from other flyers.
Updates

I would like to see some unique fonts being used, so far I have only recieved "canned" fonts, some were just straight out Adobe fonts (on a design site? Really?).

Some SUGGESTIONS would include font use similar to the following:
http://www.glyphyard.net/oldpress.font
http://www.glyphyard.net/happy-otter.font

Fun fonts, something that grabs attention.
If you're going to plonk one image in the middle of the page and fill it with text in Courier New, consider not submitting.

I would like colourful, attention grabbing backgrounds.

Target Market(s)

Families

Industry/Entity Type

Business

Requirements
Must have
• Two sides to the flyer
Focus on "fun"
Targetted to mothers
Nice to have
• All photos attached, not necessary but nice.
Should not have
• Anything too "corporate"

```html
<!DOCTYPE html>
<html lang="en">
<head>
<meta charset="utf-8">
<title>Golden Nook – Family Photography Flyer</title>
<link rel="stylesheet" href="https://fonts.googleapis.com/css2?family=Bevan&family=Didact+Gothic&display=swap">
<style>
  :root {
    --paper: #ffffff;
    --teal: #24979f;
    --teal-dark: #1d8088;
    --rose: #c96f9d;
    --ink: #111111;
    --body-ink: #2a2a2a;
    --photo-girl-a: #d9cfc6;
    --photo-girl-b: #b9a69a;
    --photo-baby-a: #8a8580;
    --photo-baby-b: #b9bec7;
    --photo-family-a: #4f6e3a;
    --photo-family-b: #a7b98e;
  }
  * { margin: 0; padding: 0; box-sizing: border-box; }
  html, body { width: 846px; height: 1200px; overflow: hidden; background: var(--paper); }
  .flyer {
    position: relative;
    width: 846px;
    height: 1200px;
    overflow: hidden;
    background: var(--paper);
  }
  .flyer__art { position: absolute; inset: 0; }
  .headline {
    position: absolute;
    left: 211px;
    top: 66px;
    font-family: "Bevan", serif;
    font-size: 28px;
    line-height: 39px;
    color: var(--ink);
    letter-spacing: 0.2px;
  }
  .photo {
    position: absolute;
    box-shadow: inset 0 0 22px 14px var(--paper);
  }
  .photo--girl {
    left: 353px; top: 259px; width: 241px; height: 304px;
    background: linear-gradient(180deg, #e8e6e2 0%, var(--photo-girl-a) 35%, var(--photo-girl-b) 70%, #c65a7a 100%);
  }
  .photo--baby {
    left: 594px; top: 155px; width: 212px; height: 315px;
    background: linear-gradient(180deg, var(--photo-baby-a) 0%, #6f6a66 40%, var(--photo-baby-b) 75%, #9aa7bd 100%);
  }
  .photo--family {
    left: 302px; top: 755px; width: 544px; height: 397px;
    background: radial-gradient(ellipse at 55% 65%, #c9a48f 0%, #8a6a55 22%, transparent 45%),
                linear-gradient(180deg, var(--photo-family-b) 0%, var(--photo-family-a) 55%, #2f3a2a 100%);
  }
  .ornament {
    position: absolute;
    left: 0; top: 225px; width: 105px; height: 280px;
    background: radial-gradient(ellipse at 40% 50%, rgba(36,151,159,0.55) 0%, rgba(36,151,159,0.15) 60%, transparent 75%);
  }
  .intro {
    position: absolute;
    left: 360px;
    top: 615px;
    width: 358px;
    font-family: "Didact Gothic", sans-serif;
    font-size: 18px;
    line-height: 24.5px;
    color: var(--body-ink);
    text-align: justify;
    text-align-last: center;
  }
  .brand-vertical {
    position: absolute;
    left: 72px;
    top: 516px;
    width: 32px;
    display: flex;
    flex-direction: column;
    align-items: center;
    font-family: "Bevan", serif;
    font-size: 30px;
    line-height: 37.5px;
    color: var(--ink);
  }
  .brand-vertical .gap { height: 37.5px; }
  .brand-mark {
    position: absolute;
    left: 31px;
    top: 1039px;
    width: 184px;
    height: 138px;
    display: flex;
    align-items: center;
    justify-content: center;
    gap: 10px;
  }
  .brand-mark__square { width: 18px; height: 18px; background: var(--ink); }
  .brand-mark__name {
    font-family: "Bevan", serif;
    font-size: 22px;
    color: var(--ink);
  }
</style>
</head>
<body>
<main class="flyer">
  <svg class="flyer__art" width="846" height="1200" viewBox="0 0 846 1200" aria-hidden="true">
    <g fill="none" stroke="var(--rose)" stroke-width="3">
      <path class="line line--left-a" d="M104,0 C140,320 250,600 392,790"/>
      <path class="line line--left-b" d="M113,0 C152,320 264,600 405,790"/>
      <path class="line line--right-a" d="M716,470 C795,560 805,680 772,757"/>
      <path class="line line--right-b" d="M738,470 C815,560 822,680 800,757"/>
      <path class="line line--top-a" d="M660,62 C690,30 720,14 745,0"/>
      <path class="line line--top-b" d="M682,62 C712,30 745,12 772,0"/>
      <path class="line line--bottom-a" d="M404,1140 C396,1170 385,1190 370,1200"/>
      <path class="line line--bottom-b" d="M498,1150 C496,1175 493,1190 490,1200"/>
    </g>
    <path class="swoosh" fill="var(--teal)"
      d="M106,0 C80,260 115,520 235,760 C300,900 330,1050 332,1200 L362,1200 C362,1010 330,860 275,720 C175,480 118,240 232,0 Z"/>
  </svg>

  <div class="ornament" role="img" aria-label="Teal floral vine ornament"></div>

  <h1 class="headline">For natural and comfortable family<br>and pregnancy photography<br>choose Golden Nook.</h1>

  <div class="photo photo--girl" role="img" aria-label="Smiling curly-haired toddler girl in a pink top by the water"></div>
  <div class="photo photo--baby" role="img" aria-label="Baby boy in a blue shirt sitting beside a large stone sculpture"></div>

  <p class="intro">Thinking about updating the family portrait? Don’t have a family portrait? Want a fresh, outdoor shoot rather than an indoor studio?</p>

  <div class="photo photo--family" role="img" aria-label="Mother with her daughter and son posing among green tropical leaves"></div>

  <div class="brand-vertical" aria-label="Golden Nook">
    <span>G</span><span>o</span><span>l</span><span>d</span><span>e</span><span>n</span>
    <span class="gap"></span>
    <span>N</span><span>o</span><span>o</span><span>k</span>
  </div>

  <div class="brand-mark">
    <span class="brand-mark__square"></span>
    <span class="brand-mark__name">Golden Nook</span>
  </div>
</main>
</body>
</html>
```